Remodel Flyer for realtors

"K" Tandem Builders

4"x 9" rack card front and back

www.BrindleyRenovator.com

555-318-4762

Let us fix what your home inspector finds!

Send us your inspection summary.

We are a licensed and Insured contractor.
CRC4871093

Serving
Marion County and The Heronfield

This flyer will sit in realtor offices for realtors to give to there buyers and sellers.

Target Market(s)

Realtors

Industry/Entity Type

Construction

Colors

Designer to choose colors to be used in the design.

```html
<!DOCTYPE html>
<html lang="en">
<head>
<meta charset="utf-8">
<title>K Tandem Builders – Rack Cards</title>
<link rel="stylesheet" href="https://fonts.googleapis.com/css2?family=Catamaran:wght@600;700;800&family=Raleway:wght@300;400;600&display=swap">
<style>
  :root {
    --orange: #ef8a0c;
    --slate: #545454;
    --ink: #333333;
    --paper: #ffffff;
    --backdrop: #c7c7c7;
  }
  html, body {
    margin: 0;
    width: 1200px;
    height: 1200px;
    overflow: hidden;
    background: var(--backdrop);
  }
  .sheet {
    position: relative;
    width: 1200px;
    height: 1200px;
  }
  .rack-card {
    position: absolute;
    top: 60px;
    width: 480px;
    height: 1080px;
    background: var(--paper);
  }
  .rack-card--front { left: 69px; }
  .rack-card--back { left: 652px; }
  .rack-card svg { display: block; width: 100%; height: 100%; }
  .brand-name { font-family: "Catamaran", sans-serif; font-weight: 800; fill: var(--ink); letter-spacing: 1px; }
  .brand-sub { font-family: "Catamaran", sans-serif; font-weight: 800; fill: var(--ink); letter-spacing: 9px; }
  .tagline-light { font-family: "Raleway", sans-serif; font-weight: 300; fill: var(--ink); }
  .tagline-bold { font-family: "Catamaran", sans-serif; font-weight: 700; fill: var(--orange); }
  .phone { font-family: "Catamaran", sans-serif; font-weight: 800; fill: var(--orange); }
  .web { font-family: "Raleway", sans-serif; font-weight: 600; fill: var(--paper); }
  .license-note { font-family: "Raleway", sans-serif; font-weight: 600; fill: var(--ink); }
  .license-number { font-family: "Raleway", sans-serif; font-weight: 300; fill: var(--orange); }
</style>
</head>
<body>
<main class="sheet">

  <section class="rack-card rack-card--front">
    <svg viewBox="0 0 600 1350" xmlns="http://www.w3.org/2000/svg">
      <defs>
        <linearGradient id="hearthTones" x1="0" y1="0" x2="0" y2="1">
          <stop offset="0" stop-color="#eee3d2"/>
          <stop offset="0.45" stop-color="#e6dccb"/>
          <stop offset="0.7" stop-color="#6a625a"/>
          <stop offset="1" stop-color="#b99a72"/>
        </linearGradient>
      </defs>
      <g class="brand">
        <rect x="278" y="62" width="44" height="44" fill="var(--orange)"/>
        <text class="brand-name" x="300" y="166" font-size="27" text-anchor="middle">"K" TANDEM</text>
        <text class="brand-sub" x="304" y="186" font-size="13" text-anchor="middle">BUILDERS</text>
      </g>
      <polygon points="0,182 300,226 0,280" fill="var(--orange)"/>
      <polygon class="photo" role="img" aria-label="Photo of a white painted fireplace mantel with framed picture, glass vases and a log basket" points="0,280 600,187 600,980 0,1073" fill="url(#hearthTones)"/>
      <line x1="0" y1="280" x2="600" y2="187" stroke="var(--slate)" stroke-width="4"/>
      <line x1="0" y1="1073" x2="600" y2="980" stroke="var(--slate)" stroke-width="4"/>
      <polygon points="330,1022 600,980 600,1070" fill="var(--orange)"/>
      <text class="tagline-light" x="300" y="1117" font-size="38" text-anchor="middle">Let us fix what your</text>
      <text class="tagline-bold" x="300" y="1170" font-size="44" text-anchor="middle">HOME INSPECTOR FINDS!</text>
      <rect x="0" y="1208" width="600" height="97" fill="var(--slate)"/>
      <text class="phone" x="300" y="1260" font-size="46" text-anchor="middle">555-318-4762</text>
      <text class="web" x="300" y="1287" font-size="21" text-anchor="middle">www.BrindleyRenovator.com</text>
    </svg>
  </section>

  <section class="rack-card rack-card--back">
    <svg viewBox="0 0 600 1350" xmlns="http://www.w3.org/2000/svg">
      <defs>
        <linearGradient id="kitchenTones" x1="0" y1="0" x2="0" y2="1">
          <stop offset="0" stop-color="#f1efec"/>
          <stop offset="0.6" stop-color="#f4f2ef"/>
          <stop offset="1" stop-color="#e6e2dc"/>
        </linearGradient>
        <linearGradient id="tableFade" x1="0" y1="0" x2="0" y2="1">
          <stop offset="0" stop-color="#f3f3f3"/>
          <stop offset="1" stop-color="#ffffff"/>
        </linearGradient>
      </defs>
      <g class="brand">
        <rect x="283" y="58" width="34" height="34" fill="var(--orange)"/>
        <text class="brand-name" x="300" y="138" font-size="20" text-anchor="middle">"K" TANDEM</text>
        <text class="brand-sub" x="302" y="154" font-size="10" text-anchor="middle">BUILDERS</text>
      </g>
      <polygon points="330,200 600,158 600,245" fill="var(--slate)"/>
      <polygon class="photo" role="img" aria-label="Photo of a bright kitchen with pendant lamps, a framed mirror and a vase of sunflowers" points="0,155 600,245 600,805 0,715" fill="url(#kitchenTones)"/>
      <polygon points="0,715 230,750 0,795" fill="var(--slate)"/>
      <rect class="photo-fade" role="img" aria-label="Faded photo of a white dining table and chairs" x="0" y="795" width="600" height="413" fill="url(#tableFade)"/>
      <polygon points="0,715 600,805 600,805 0,795" fill="none"/>
      <line x1="0" y1="155" x2="600" y2="245" stroke="var(--orange)" stroke-width="5"/>
      <line x1="0" y1="715" x2="600" y2="805" stroke="var(--orange)" stroke-width="5"/>
      <polygon points="80,950 195,947 195,953" fill="var(--ink)"/>
      <polygon points="520,950 405,947 405,953" fill="var(--ink)"/>
      <text class="tagline-bold" x="300" y="963" font-size="54" text-anchor="middle">Serving</text>
      <text class="tagline-light" x="300" y="1019" font-size="35" text-anchor="middle">Marion County &amp; The Heronfield</text>
      <text class="license-note" x="300" y="1090" font-size="25" text-anchor="middle">We are a licensed &amp; Insured contractor</text>
      <text class="license-number" x="300" y="1143" font-size="48" text-anchor="middle">CRC4871093</text>
      <text class="tagline-light" x="300" y="1187" font-size="29" text-anchor="middle" style="font-weight:400">Send us your inspection summary</text>
      <rect x="0" y="1208" width="600" height="97" fill="var(--slate)"/>
      <text class="phone" x="300" y="1260" font-size="46" text-anchor="middle">555-318-4762</text>
      <text class="web" x="300" y="1287" font-size="21" text-anchor="middle">www.BrindleyRenovator.com</text>
    </svg>
  </section>

</main>
</body>
</html>
```